Gentle Harbor Label

We need labels for a new brewery called "Gentle Harbor":

We need one label, that we can slightly change to suit the style of liquid. So far the beers are:
- XPA
- Pale ALe
- IPA
- Black Ale

We want creative, fun labels, nothing traditional. but appropriate to suit all international markets.

Design was promoted in LOGO & not in Design, so we got a lot of logo's but very little designs for bottles/cans.

Gentle Harbor Brewing

```html
<!DOCTYPE html>
<html lang="en">
<head>
<meta charset="utf-8">
<title>Gentle Harbor Brewing – Pale Ale Label</title>
<link href="https://fonts.googleapis.com/css2?family=Russo+One&family=Arimo:wght@400;700&display=swap" rel="stylesheet">
<style>
  :root {
    --page: #ffffff;
    --paper-light: #e4e4e4;
    --paper-mid: #cfcfcf;
    --paper-edge: #b9b9b9;
    --ink: #1d1d1b;
    --band-blue: #3aa3d6;
    --band-blue-deep: #1f7fbf;
    --ribbon-start: #1b7fcc;
    --ribbon-end: #a9dcf7;
    --ribbon-curl: #0e5fae;
  }
  html, body {
    margin: 0;
    padding: 0;
    width: 1200px;
    height: 1200px;
    overflow: hidden;
    background: var(--page);
  }
  .label {
    display: block;
    width: 1200px;
    height: 1200px;
  }
  .paper { fill: url(#paperTone); stroke: var(--paper-edge); stroke-width: 1; }
  .sheet-fold { stroke: #a8a8a8; stroke-width: 2; fill: none; }
  .brand-band { fill: url(#bandTone); }
  .ribbon { fill: url(#ribbonTone); }
  .ribbon-curl { fill: var(--ribbon-curl); }
  .brand-name {
    font-family: "Russo One", sans-serif;
    font-size: 150px;
    fill: var(--ink);
  }
  .brewery-line {
    font-family: "Russo One", sans-serif;
    font-size: 42px;
    letter-spacing: 1px;
    fill: var(--ink);
  }
  .style-name {
    font-family: "Arimo", sans-serif;
    font-weight: 700;
    font-size: 76px;
    fill: var(--ink);
  }
  .info-text {
    font-family: "Arimo", sans-serif;
    font-size: 24px;
    fill: var(--ink);
  }
</style>
</head>
<body>
<svg class="label" viewBox="0 0 1200 1200" xmlns="http://www.w3.org/2000/svg" role="group" aria-label="Gentle Harbor Pale Ale label">
  <defs>
    <linearGradient id="paperTone" x1="0" y1="0" x2="1" y2="1">
      <stop offset="0" stop-color="var(--paper-light)"/>
      <stop offset="1" stop-color="var(--paper-mid)"/>
    </linearGradient>
    <linearGradient id="bandTone" x1="0" y1="0" x2="1" y2="0">
      <stop offset="0" stop-color="#5cb8de"/>
      <stop offset="1" stop-color="var(--band-blue-deep)"/>
    </linearGradient>
    <linearGradient id="ribbonTone" x1="0" y1="0" x2="1" y2="0">
      <stop offset="0" stop-color="var(--ribbon-start)"/>
      <stop offset="1" stop-color="var(--ribbon-end)"/>
    </linearGradient>
  </defs>

  <!-- top sheet with torn right edge -->
  <path class="paper" d="M212 110 L950 112 L948 150 L956 170 L950 210 L958 240 L952 290 L960 330 L954 380 L962 430 L956 480 L964 530 L958 580 L966 630 L960 680 L968 730 L962 770 L272 772 L268 700 L216 706 L218 600 L210 500 L216 400 L210 300 L214 200 Z"/>
  <line class="sheet-fold" x1="208" y1="416" x2="954" y2="348"/>

  <!-- brand name -->
  <text class="brand-name" x="590" y="330" text-anchor="middle">Gentle</text>
  <text class="brand-name" x="590" y="500" text-anchor="middle">Harbor</text>

  <!-- blue brewery band -->
  <path class="brand-band" d="M266 594 L842 578 L916 626 L906 736 L276 742 L250 822 L242 812 L262 700 Z"/>
  <text class="brewery-line" x="592" y="690" text-anchor="middle" transform="rotate(2 592 690)">Craft Beer Brewery</text>

  <!-- lower sheet -->
  <path class="paper" d="M278 742 L940 738 L936 790 L944 840 L938 900 L946 960 L940 1020 L946 1090 L282 1092 L276 1040 L282 980 L276 900 L282 820 Z"/>

  <!-- style ribbon -->
  <path class="ribbon" d="M292 822 L858 760 L846 808 L820 850 L804 866 L326 926 Z"/>
  <path class="ribbon-curl" d="M858 760 C852 800 838 836 804 866 C826 850 840 840 852 836 C850 810 854 784 858 760 Z"/>
  <text class="style-name" x="570" y="876" text-anchor="middle" transform="rotate(-6 570 876)">Pale Ale</text>

  <!-- info -->
  <text class="info-text" x="598" y="965" text-anchor="middle">Some information to be placed in this area.</text>
  <text class="info-text" x="598" y="997" text-anchor="middle">Brewed to perfection</text>
  <text class="info-text" x="598" y="1056" text-anchor="middle">4.5% Alc./Vol</text>
</svg>
</body>
</html>
```